Coldmerrow Brochure & Fact Sheet

We need a brochure designed that we will distribute both digitally (PDF) and also have printed. We our an IT company and would like the creative to reflect our brand and industry. All content is written and ready to go. We need each page of the brochure provided as an individual file so we can arrange the pages as needed.

```html
<!DOCTYPE html>
<html lang="en">
<head>
<meta charset="utf-8">
<title>Coldmerrow Brochure &amp; Fact Sheet</title>
<link href="https://fonts.googleapis.com/css2?family=Montserrat:wght@300;400;600;700&display=swap" rel="stylesheet">
<style>
  :root {
    --backdrop: #b3e0e7;
    --paper: #ffffff;
    --ink: #1d1d1d;
    --ink-soft: #555555;
    --rule: #2a2a2a;
    --band: #333333;
    --row-alt: #ececec;
    --grey-ring: #d9d9d9;
  }
  * { box-sizing: border-box; margin: 0; padding: 0; }
  html, body { width: 1200px; height: 2889px; overflow: hidden; }
  body {
    background: var(--backdrop);
    font-family: "Montserrat", sans-serif;
    color: var(--ink);
    position: relative;
  }
  .page {
    position: absolute;
    left: 320px;
    width: 560px;
    height: 725px;
    background: var(--paper);
    padding: 40px 42px;
  }
  .page--cover { top: 118px; }
  .page--facts { top: 1082px; }
  .page--services { top: 2046px; }

  .corner-mark {
    position: absolute;
    left: 0; top: 44px;
    width: 22px; height: 22px;
    background: var(--ink);
  }
  .cover-title {
    margin-left: 10px;
    font-weight: 300;
    font-size: 21px;
    line-height: 1.15;
    letter-spacing: 0.5px;
    text-transform: uppercase;
  }
  .cover-title strong { font-weight: 700; }
  .cover-rule {
    margin: 14px 0 0 -42px;
    width: 470px;
    height: 2px;
    background: var(--rule);
  }
  .cover-art { position: absolute; left: 60px; top: 120px; }
  .brand {
    display: flex; align-items: center; gap: 8px;
    font-weight: 700; font-size: 20px; color: var(--ink);
  }
  .brand-square { width: 16px; height: 16px; background: var(--ink); }
  .cover-badge {
    position: absolute; left: 325px; top: 365px;
    width: 170px; height: 170px; border-radius: 50%;
    background: var(--paper);
    border: 1px solid #bdbdbd;
    display: flex; align-items: center; justify-content: center;
  }

  .page-heading {
    margin-left: 10px;
    font-size: 17px; font-weight: 600; line-height: 1.15;
  }
  .page-heading strong { font-weight: 700; }
  .body-copy {
    font-size: 6.4px; line-height: 1.5; color: var(--ink-soft);
    margin-top: 8px;
  }
  .body-copy b { color: var(--ink); }

  .facts-table {
    margin: 14px 18px 0;
    border: 1px solid #bbbbbb;
    border-radius: 8px;
    overflow: hidden;
    font-size: 6.2px;
  }
  .facts-table caption, .facts-head {
    background: var(--band); color: #fff;
    text-align: center; font-size: 7px; letter-spacing: 1.5px;
    padding: 5px 0; font-weight: 600;
  }
  .facts-table table { width: 100%; border-collapse: collapse; }
  .facts-table td { padding: 4px 10px; vertical-align: top; line-height: 1.45; color: var(--ink-soft); }
  .facts-table td:first-child { width: 38%; color: var(--ink); }
  .facts-table tr:nth-child(odd) td { background: var(--row-alt); }

  .footer-brand { position: absolute; right: 42px; }
  .footer-rule {
    position: absolute; left: 0; bottom: 36px;
    width: 330px; height: 3px; background: var(--rule);
  }

  .approach-band {
    margin-top: 10px;
    background: var(--band); color: #fff;
    font-size: 6.6px; font-weight: 600;
    padding: 4px 14px; display: inline-block;
  }
  .service { margin-top: 7px; }
  .service h3 { font-size: 6.8px; font-weight: 700; letter-spacing: 0.3px; }
  .service p { font-size: 6.2px; line-height: 1.5; color: var(--ink-soft); }
</style>
</head>
<body>

<section class="page page--cover">
  <span class="corner-mark"></span>
  <h1 class="cover-title">Harness the potential<br>of technology with <strong>Coldmerrow</strong></h1>
  <div class="cover-rule"></div>

  <svg class="cover-art" width="440" height="440" viewBox="0 0 440 440">
    <defs>
      <radialGradient id="ringFade" cx="50%" cy="50%" r="50%">
        <stop offset="70%" stop-color="#ffffff"/>
        <stop offset="100%" stop-color="#e4e4e4"/>
      </radialGradient>
      <linearGradient id="photoTone" x1="0" y1="0" x2="0" y2="1">
        <stop offset="0" stop-color="#eef1f3"/>
        <stop offset="0.55" stop-color="#8c8f93"/>
        <stop offset="1" stop-color="#3a3c40"/>
      </linearGradient>
    </defs>
    <circle cx="200" cy="200" r="198" fill="url(#ringFade)"/>
    <circle cx="200" cy="200" r="150" fill="none" stroke="#222" stroke-width="1.5"/>
    <circle cx="200" cy="200" r="138" fill="url(#photoTone)" role="img" aria-label="Photo of a cheering office team raising their arms in celebration"/>
  </svg>
  <div class="cover-badge"><span class="brand"><span class="brand-square"></span>coldmerrow</span></div>
</section>

<section class="page page--facts">
  <span class="corner-mark" style="top:40px"></span>
  <h2 class="page-heading">Harness the Potential<br>of Technology with <strong>Coldmerrow</strong></h2>
  <p class="body-copy">We believe that technology has the potential to change how every business works. It is not a box of parts; it is a tool that helps people do great work. When it runs well, nobody notices. <b>And that's why we're here.</b></p>
  <p class="body-copy">It's when you combine a robust tech platform with smart, informed ideas that results follow. Our team brings years of hands-on practice to every project we take on.</p>
  <p class="body-copy">At Coldmerrow, our team has a reputation for being proactive, proven and easy to work with. We see technology as a partner in your growth and stay with you at every step, so your people can <b>understand, value, and feel empowered to implement.</b></p>

  <div class="facts-table">
    <div class="facts-head">COLDMERROW FACTS</div>
    <table>
      <tr><td>Established</td><td>2000</td></tr>
      <tr><td>Headquarters</td><td>48 Lantern Row NW, Harlow Bay, NH 03301</td></tr>
      <tr><td>Executive Leadership</td><td>Ada Renwick, CEO<br>Tomas Vell, COO<br>Nina Arden, Client Services<br>Paul Marsh, Sales &amp; Marketing</td></tr>
      <tr><td>Team Members</td><td>25</td></tr>
      <tr><td>Combined Staff Experience</td><td>85+ Years</td></tr>
      <tr><td>Core Services</td><td>Full Service Managed IT Services, Software, Website Development, IT Consulting</td></tr>
      <tr><td>Accolades</td><td>Regional 101 Best &amp; Brightest 2014<br>Service Provider 501 2015<br>Sector Top 50 Firm 2016<br>Sector Top 50 Firm 2017<br>Sector Top 50 Firm 2018</td></tr>
      <tr><td>Certifications</td><td>Certified Cloud Partner<br>Network Security Partner<br>Virtualization Partner<br>Storage Specialist<br>Backup Certified Partner</td></tr>
    </table>
  </div>

  <div class="footer-brand" style="bottom:70px"><span class="brand"><span class="brand-square"></span>coldmerrow</span></div>
  <div class="footer-rule"></div>
</section>

<section class="page page--services">
  <span class="corner-mark" style="top:40px"></span>
  <h2 class="page-heading">Coldmerrow Managed IT Services</h2>
  <p class="body-copy">Managed Services by Coldmerrow deliver steady, predictable support for growing teams. We watch your systems around the clock, solve problems before they spread and keep your costs clear. Our engineers plan, build and care for your network so that your staff can focus on the work that matters most to your business every day.</p>

  <div class="approach-band">Our Managed IT Services Approach</div>

  <div class="service"><h3>INFRASTRUCTURE</h3><p>We specialize in architecting a streamlined IT system that works harmoniously with your business. We monitor servers, storage and networks daily, apply updates on schedule and keep every layer documented so nothing is left to chance.</p></div>
  <div class="service"><h3>SECURITY</h3><p>Our security services include endpoint protection, network defense, email filtering and staff training. We review threats as they appear and respond quickly, keeping your data and your clients safe and your team confident online.</p></div>
  <div class="service"><h3>DISASTER RECOVERY</h3><p>No matter how well protected you are, it's better to plan for the unexpected. We design backup and recovery plans, test them often and make sure your business can return to work fast after any outage.</p></div>
  <div class="service"><h3>DESKTOP MANAGEMENT</h3><p>We help your employees focus on the day-to-day business at hand by keeping every workstation current, secure and running well. Our help desk answers support questions and resolves issues for your staff 24/7.</p></div>
  <div class="service"><h3>CLOUD MANAGEMENT</h3><p>Valuable business data needs to be stored and protected. We help businesses choose the right cloud model and move their systems with care, then manage and monitor every account for you.</p></div>
  <div class="service"><h3>CUSTOMER SERVICE IS AT THE CORE OF OUR COLDMERROW TEAM</h3><p>Our Managed IT Services are successful because we have a dedicated and experienced team ensuring your staff receives rapid responses and expert support from technicians they know and trust.</p></div>

  <div class="footer-brand" style="bottom:70px"><span class="brand"><span class="brand-square"></span>coldmerrow</span></div>
  <div class="footer-rule"></div>
</section>

</body>
</html>
```